Business Cards for Bramblewood Coatings Pty Ltd

Hi every one i need a design for my buisness cards. I Want my logo in it and the name of the company needs to stand out Bramblewood Coatings Pty Ltd. I want the background of the buisness cards black and i want the font to stand out in either a white or a silver stylish text. I want the design to be simple but original not to in your face if you know what i mean. I want on the back of the buisness cards to have the services that my buisness offers.
• Interior/Exterior
• Residential/Commercial
• Special effects/Texture Coatings
• Water Damage Repair
• Fully qualified
• Pensioner Discount
• 10 Year guarantee
• Fully Insured
• Obligation free quotes
full internal repaints include a proffesionla cleaning service
I want the services on the back to be layed out in an originall way not just dot points. If possible could my logo take up the whole back ground of the back but the text with the services be kind of like transparent so u cvan still see the logo i dont know if its possible it woiuld just look cool if possible. When i pick a design ill give my contact details to the designer to add to the design at the end. Any questions please just ask! Ill upload my logo.
Conatcs will include office phone: Mobile: E-mail - dean@bramblewoodcoatings.com.au, Ill also have a Postal address which is a PO Box and my website is www.bramblewoodcoatings.com.au

```html
<!DOCTYPE html>
<html lang="en">
<head>
<meta charset="utf-8">
<title>Bramblewood Coatings – Business Card</title>
<link rel="stylesheet" href="https://fonts.googleapis.com/css2?family=Montserrat:wght@300;600;700&family=Questrial&family=Cormorant+Garamond:wght@500&display=swap">
<style>
  :root {
    --stage: #d2d2d2;
    --card: #050505;
    --lime: #8cc63e;
    --lime-glow: #b6f24a;
    --silver: #e6e6e6;
    --white: #ffffff;
    --label: #333333;
  }
  * { margin: 0; padding: 0; box-sizing: border-box; }
  html, body { width: 1200px; height: 765px; overflow: hidden; }
  body { background: var(--stage); position: relative; }
  .card { position: absolute; top: 302px; width: 574px; height: 343px; }
  .card--front { left: 16px; }
  .card--back { left: 604px; }
  .card svg { display: block; width: 574px; height: 343px; }
  .side-label {
    position: absolute; top: 684px;
    font-family: "Cormorant Garamond", serif; font-weight: 500;
    font-size: 15px; letter-spacing: 3px; color: var(--label);
  }
  .side-label--front { left: 66px; }
  .side-label--back { left: 659px; }

  .holder-name { font-family: "Montserrat", sans-serif; font-weight: 300; font-size: 31px; letter-spacing: 4px; fill: var(--white); }
  .company-name { font-family: "Montserrat", sans-serif; font-weight: 700; font-size: 19px; fill: var(--silver); }
  .contact { font-family: "Montserrat", sans-serif; font-weight: 600; font-size: 10px; fill: var(--white); }
  .contact-label { font-weight: 300; }
  .postal { font-family: "Montserrat", sans-serif; font-weight: 600; font-size: 7.5px; fill: var(--silver); letter-spacing: .5px; }

  .service { font-family: "Questrial", sans-serif; fill: var(--lime); }
  .service--xl { font-size: 29px; }
  .service--lg { font-size: 21px; }
  .service--md { font-size: 15px; }
  .service--sm { font-size: 11px; }
  .service--xs { font-size: 8px; }
  .back-company { font-family: "Montserrat", sans-serif; font-weight: 700; font-size: 8.5px; fill: var(--silver); }
</style>
</head>
<body>

<div class="card card--front">
  <svg viewBox="0 0 574 343" xmlns="http://www.w3.org/2000/svg">
    <defs>
      <clipPath id="front-shape"><rect width="574" height="343" rx="38"/></clipPath>
      <linearGradient id="silver-band" x1="0" y1="0" x2="1" y2="0">
        <stop offset="0" stop-color="#ffffff" stop-opacity="0"/>
        <stop offset=".55" stop-color="#ffffff" stop-opacity=".22"/>
        <stop offset="1" stop-color="#ffffff" stop-opacity=".55"/>
      </linearGradient>
      <linearGradient id="lime-band" x1="0" y1="0" x2="1" y2="0">
        <stop offset="0" stop-color="#b6f24a" stop-opacity=".9"/>
        <stop offset=".5" stop-color="#8cc63e" stop-opacity=".45"/>
        <stop offset="1" stop-color="#d9ff7a" stop-opacity=".95"/>
      </linearGradient>
      <filter id="soft-glow" x="-50%" y="-50%" width="200%" height="200%">
        <feGaussianBlur stdDeviation="6"/>
      </filter>
    </defs>
    <g clip-path="url(#front-shape)">
      <rect class="card-base" width="574" height="343" fill="var(--card)"/>
      <g class="light-bands" transform="rotate(-14 287 171)">
        <rect x="-80" y="95" width="740" height="70" fill="url(#silver-band)" opacity=".35"/>
        <rect x="-80" y="186" width="740" height="14" fill="url(#lime-band)" filter="url(#soft-glow)"/>
        <rect x="-80" y="191" width="740" height="3" fill="var(--lime-glow)"/>
        <rect x="-80" y="208" width="740" height="2" fill="url(#silver-band)"/>
        <rect x="-80" y="160" width="740" height="2" fill="url(#silver-band)"/>
        <rect x="-80" y="300" width="740" height="2" fill="url(#silver-band)"/>
        <rect x="-80" y="214" width="740" height="80" fill="#ffffff" opacity=".05"/>
      </g>
      <rect class="brand-square-glow" x="62" y="102" width="104" height="104" rx="14" fill="var(--lime)" opacity=".55" filter="url(#soft-glow)" transform="rotate(-6 114 154)"/>
      <rect class="brand-square" x="70" y="110" width="88" height="88" rx="10" fill="var(--lime)" transform="rotate(-6 114 154)"/>
      <text class="holder-name" transform="translate(222 132) rotate(-13)">DEAN HARLOW</text>
      <g class="company-name-block" transform="translate(36 258) rotate(-13)">
        <text class="company-name" x="0" y="0">BRAMBLEWOOD</text>
        <text class="company-name" x="0" y="22">COATINGS PTY LTD</text>
      </g>
      <g class="contact-block" transform="translate(250 228) rotate(-13)">
        <text class="contact" x="0" y="0"><tspan class="contact-label">TEL : </tspan>0198765432</text>
        <text class="contact" x="0" y="12"><tspan class="contact-label">MOB : </tspan>0198765432</text>
        <text class="contact" x="0" y="24"><tspan class="contact-label">EMAIL : </tspan>DEAN@BRAMBLEWOODCOATINGS.COM.AU</text>
        <text class="contact" x="0" y="36"><tspan class="contact-label">WEBSITE : </tspan>WWW.BRAMBLEWOODCOATINGS.COM.AU</text>
        <text class="postal" x="10" y="52">PO BOX ADDRESS 12345 LOREMIPSUM DOLOR</text>
      </g>
    </g>
  </svg>
</div>

<div class="card card--back">
  <svg viewBox="0 0 574 343" xmlns="http://www.w3.org/2000/svg">
    <defs>
      <clipPath id="back-shape"><rect width="574" height="343" rx="38"/></clipPath>
      <linearGradient id="back-silver" x1="0" y1="0" x2="1" y2="0">
        <stop offset="0" stop-color="#ffffff" stop-opacity=".05"/>
        <stop offset=".6" stop-color="#ffffff" stop-opacity=".3"/>
        <stop offset="1" stop-color="#ffffff" stop-opacity=".75"/>
      </linearGradient>
    </defs>
    <g clip-path="url(#back-shape)">
      <rect class="card-base" width="574" height="343" fill="var(--card)"/>
      <g class="light-bands" transform="rotate(-14 287 171)">
        <rect x="-80" y="50" width="740" height="70" fill="url(#back-silver)" opacity=".35"/>
        <rect x="-80" y="104" width="740" height="3" fill="url(#back-silver)"/>
        <rect x="-80" y="140" width="740" height="3" fill="url(#back-silver)"/>
        <rect x="-80" y="146" width="740" height="22" fill="#ffffff" opacity=".06"/>
      </g>
      <text class="service service--lg" transform="translate(46 108) rotate(-13)">INTERIOR/EXTERIOR</text>
      <text class="service service--sm" transform="translate(194 94) rotate(-13)">RESIDENTIAL/COMMERCIAL</text>
      <text class="service service--md" transform="translate(188 176) rotate(-13)">SPECIAL EFFECTS/TEXTURE COATINGS</text>
      <g class="back-brand" transform="translate(84 150) rotate(-10)">
        <rect class="brand-square" x="6" y="0" width="30" height="30" rx="4" fill="var(--lime)"/>
        <text class="back-company" x="0" y="43">BRAMBLEWOOD</text>
        <text class="back-company" x="0" y="54">COATINGS PTY LTD</text>
      </g>
      <text class="service service--md" transform="translate(36 256) rotate(-13)">WATER DAMAGE REPAIR</text>
      <text class="service service--xl" transform="translate(206 222) rotate(-13)">FULLY QUALIFIED</text>
      <text class="service service--lg" transform="translate(306 232) rotate(-13)">PENSIONER DISCOUNT</text>
      <text class="service service--lg" transform="translate(62 292) rotate(-13)">10 YEAR GUARANTEE</text>
      <text class="service service--sm" transform="translate(216 282) rotate(-13)">FULLY INSURED</text>
      <text class="service service--md" transform="translate(318 262) rotate(-13)">OBLIGATION FREE QUOTES</text>
      <text class="service service--xs" transform="translate(228 314) rotate(-13)">FULL INTERNAL REPAINTS INCLUDE A PROFESSIONAL CLEANING SERVICE</text>
    </g>
  </svg>
</div>

<p class="side-label side-label--front">FRONT</p>
<p class="side-label side-label--back">BACK</p>

</body>
</html>
```